Gutschein-Design für Verkauf von Online-Schmuckstücken
Zielgruppe
Wir verkaufen Online Schmuckstücke!
www.feldring-atelier.example
Aufgabenstellung
Wir haben eine schwarze Schachtel erstellt und da drinne wird eine Geschenkgutschein sein:
Es soll sehr schlicht sein und schwarzen Hintergrund haben.
Vorderseite nur unser LOGO.
Rückseite:
Betrag: _________
Gültig Bis: _________
Code: __________
Und unten klein gedruckt steht:
Diese Karte ist gültig nur auf der online shop seite www.feldring-atelier.example und in unserer offizielen Stores. Dieses Karte ist nicht gültig bei rabatierte Produkten und man kann nicht mit dieser karte einen Gutscheinkarte kaufen.
Der Design soll sehr schlicht und dezenz sein.

```html
<!DOCTYPE html>
<html lang="de">
<head>
<meta charset="utf-8">
<title>Feldring Atelier – Geschenkgutschein</title>
<link rel="stylesheet" href="https://fonts.googleapis.com/css2?family=Source+Sans+3:wght@400;600&display=swap">
<style>
  :root {
    --page: #ffffff;
    --card-dark: #141414;
    --card-mid: #2a2a2a;
    --gold: #d4a43c;
    --gold-soft: #c9a24a;
    --field: #ffffff;
  }
  * { margin: 0; padding: 0; box-sizing: border-box; }
  html, body {
    width: 1200px;
    height: 600px;
    overflow: hidden;
    background: var(--page);
    font-family: "Source Sans 3", "Myriad Pro", Arial, sans-serif;
  }
  .sheet {
    position: relative;
    width: 1200px;
    height: 600px;
    display: flex;
    align-items: center;
    justify-content: center;
    gap: 40px;
  }
  .voucher {
    position: relative;
    width: 540px;
    height: 349px;
    background: radial-gradient(ellipse at 50% 42%, var(--card-mid) 0%, var(--card-dark) 72%);
    box-shadow: 6px 8px 10px rgba(0, 0, 0, 0.28);
    color: var(--gold);
  }
  /* Vorderseite */
  .voucher--front {
    display: flex;
    flex-direction: column;
    align-items: center;
    justify-content: center;
    gap: 16px;
  }
  .brand-dot {
    width: 92px;
    height: 92px;
    border-radius: 50%;
    background: var(--gold);
  }
  .brand-name {
    font-size: 42px;
    font-weight: 400;
    letter-spacing: 0.5px;
    color: var(--gold);
  }
  /* Rückseite */
  .field-label {
    position: absolute;
    font-size: 16px;
    font-weight: 400;
    text-transform: uppercase;
    color: var(--gold);
    letter-spacing: 0.2px;
  }
  .field-box {
    position: absolute;
    height: 38px;
    background: var(--field);
    box-shadow: 3px 4px 5px rgba(0, 0, 0, 0.45);
  }
  .label-amount { left: 46px; top: 118px; }
  .label-valid  { left: 275px; top: 118px; }
  .label-code   { left: 46px; top: 190px; }
  .box-amount { left: 46px; top: 139px; width: 218px; }
  .box-valid  { left: 275px; top: 139px; width: 218px; }
  .box-code   { left: 46px; top: 211px; width: 447px; }
  .fine-print {
    position: absolute;
    left: 40px;
    right: 40px;
    top: 282px;
    text-align: center;
    font-size: 10px;
    line-height: 13.5px;
    color: var(--gold-soft);
  }
</style>
</head>
<body>
  <main class="sheet">
    <section class="voucher voucher--front" aria-label="Gutschein Vorderseite">
      <div class="brand-dot"></div>
      <div class="brand-name">Feldring Atelier</div>
    </section>

    <section class="voucher voucher--back" aria-label="Gutschein Rückseite">
      <span class="field-label label-amount">Betrag:</span>
      <span class="field-label label-valid">Gültig bis:</span>
      <div class="field-box box-amount"></div>
      <div class="field-box box-valid"></div>
      <span class="field-label label-code">Code:</span>
      <div class="field-box box-code"></div>
      <p class="fine-print">
        Dieser Gutschein ist nur im Onlineshop www.feldring-atelier.example und in unseren<br>
        offiziellen Stores gültig. Der Gutschein ist nicht für bereits rabattierte Produkte<br>
        gültig und kann nicht für den Kauf einer Gutscheinkarte genutzt werden.
      </p>
    </section>
  </main>
</body>
</html>
```